Design a business card & stationary for a mortgage company

We are looking for a good looking business card design for our mortgage company that includes our logo. We received a free design as part of our logo project but we don't love it. The company is called "Pinecrest Mortgage Company" so we like waves and lighthouses. The logo should be included. We have a version in both vertical and horizontal that we have provided.

Industry/Entity Type

Finance

Contact Information for Business Card

This should include our new logo file

Requirements
Must have
• 3. The details you'd like on the card - name, title, phone, email, website, address, social media handles etc.
1. Marcus Hale
Vice President
732-419-6253
Fax 888-304-2918
mhale@pinecrestmortgage.example
NMLS 47162 - Company NMLS 61290
18 Larkin Ave
Toms River, NJ 08614

```html
<!DOCTYPE html>
<html lang="en">
<head>
<meta charset="utf-8">
<title>Pinecrest Mortgage Company – Business Card</title>
<link rel="stylesheet" href="https://fonts.googleapis.com/css2?family=Arimo:wght@400;700&display=swap">
<style>
  :root {
    --navy: #142f78;
    --blue: #1784c2;
    --white: #ffffff;
    --paper: #fbfbfb;
    --backdrop: #e4e6e8;
    --rule: #cfd6e6;
  }
  * { box-sizing: border-box; margin: 0; padding: 0; }
  html, body { width: 1200px; height: 960px; overflow: hidden; }
  body {
    background: var(--backdrop);
    font-family: "Arimo", Arial, sans-serif;
    display: flex;
    flex-direction: column;
    align-items: center;
    justify-content: center;
    gap: 60px;
  }
  .card {
    position: relative;
    width: 620px;
    height: 354px;
    border-radius: 4px;
    overflow: hidden;
    box-shadow: 0 6px 18px rgba(0,0,0,0.18);
  }

  /* Front */
  .card-front { background: var(--paper); }
  .front-logo {
    position: absolute;
    left: 0; right: 0; top: 138px;
    display: flex;
    align-items: center;
    justify-content: center;
    gap: 14px;
  }
  .logo-dot {
    width: 22px; height: 22px;
    border-radius: 50%;
    background: var(--blue);
  }
  .logo-name {
    color: var(--navy);
    font-weight: 700;
    font-size: 30px;
    letter-spacing: 0.5px;
  }
  .front-band {
    position: absolute;
    left: 48px; right: 0; bottom: 0;
    height: 16px;
    background: var(--navy);
    border-top-left-radius: 14px;
  }

  /* Back */
  .card-back { background: var(--navy); color: var(--white); }
  .holder {
    position: absolute;
    left: 0; top: 64px;
    width: 312px;
    text-align: right;
  }
  .holder-name {
    font-weight: 700;
    font-size: 27px;
    line-height: 1;
  }
  .holder-title {
    margin-top: 6px;
    font-size: 12px;
    letter-spacing: 2px;
  }
  .holder-rule {
    position: absolute;
    left: 10px; top: 124px;
    width: 302px; height: 5px;
    border-top: 2px solid var(--white);
    border-bottom: 1px solid var(--rule);
  }
  .phone-bar {
    position: absolute;
    left: 14px; top: 146px;
    width: 318px; height: 74px;
    background: var(--blue);
    padding: 10px 0 0 78px;
  }
  .phone-main {
    font-weight: 700;
    font-size: 30px;
    line-height: 1.05;
  }
  .phone-fax {
    margin-top: 6px;
    font-weight: 700;
    font-size: 17px;
  }
  .details {
    position: absolute;
    left: 94px; top: 238px;
    font-size: 12.5px;
    line-height: 1.3;
  }
  .email {
    position: absolute;
    left: 96px; top: 318px;
    font-weight: 700;
    font-size: 13px;
  }
</style>
</head>
<body>
  <section class="card card-front" aria-label="Card front">
    <div class="front-logo">
      <span class="logo-dot"></span>
      <span class="logo-name">Pinecrest Mortgage Company</span>
    </div>
    <div class="front-band"></div>
  </section>

  <section class="card card-back" aria-label="Card back">
    <div class="holder">
      <p class="holder-name">Marcus Hale</p>
      <p class="holder-title">Vice President</p>
    </div>
    <div class="holder-rule"></div>
    <div class="phone-bar">
      <p class="phone-main">732-419-6253</p>
      <p class="phone-fax">Fax 888-304-2918</p>
    </div>
    <div class="details">
      <p>NMLS 47162 - Company NMLS</p>
      <p>61290</p>
      <p>18 Larkin Ave</p>
      <p>Toms River, NJ 08614</p>
    </div>
    <p class="email">mhale@pinecrestmortgage.example</p>
  </section>
</body>
</html>
```